Modernise Business Card

Our company has been operating for 10 years. With the start of the new decade we are looking to refresh our business card design. We manufacture a range of industrial product shipping to customers internationally. A copy of our current card, both sides, is attached. We are looking for a mature professional appearance.

```html
<!DOCTYPE html>
<html lang="en">
<head>
<meta charset="utf-8">
<title>Vantrel Business Card</title>
<link href="https://fonts.googleapis.com/css2?family=Poppins:wght@300;400;600;700;800&display=swap" rel="stylesheet">
<style>
  :root {
    --bg: #e6e3de;
    --card: #ffffff;
    --blue: #00b2dd;
    --dark: #2a2220;
    --text: #2b2b2b;
  }
  * { margin: 0; padding: 0; box-sizing: border-box; }
  html, body { width: 900px; height: 1200px; overflow: hidden; }
  body {
    background: var(--bg);
    font-family: "Poppins", Arial, sans-serif;
    color: var(--text);
    position: relative;
  }
  .card {
    position: absolute;
    left: 82px;
    width: 733px;
    height: 430px;
    background: var(--card);
    border-radius: 24px;
    overflow: hidden;
    box-shadow: 0 4px 12px rgba(0,0,0,0.25);
  }
  .card--front { top: 137px; }
  .card--back { top: 633px; }
  .card__swoosh { position: absolute; inset: 0; width: 733px; height: 430px; }
  .brand {
    position: absolute;
    font-weight: 800;
    color: var(--blue);
    letter-spacing: -1px;
    line-height: 1;
  }
  .card--front .brand { left: 45px; top: 66px; font-size: 70px; }
  .card--back .brand { left: 58px; top: 56px; font-size: 72px; }
  .holder-name {
    position: absolute;
    left: 44px; top: 236px;
    font-size: 22px; font-weight: 600;
  }
  .contact-list, .address {
    position: absolute;
    list-style: none;
    font-size: 15.5px; font-weight: 400;
  }
  .contact-list { left: 44px; top: 276px; }
  .contact-list li {
    display: flex; align-items: center;
    height: 29px;
  }
  .icon {
    width: 18px; height: 18px; flex: none;
    margin-right: 11px;
  }
  .address { left: 333px; top: 305px; display: flex; }
  .address .icon { margin-top: 3px; margin-right: 10px; }
  .address p { line-height: 29px; }
  .product-list {
    position: absolute;
    left: 58px; top: 188px;
    list-style: none;
  }
  .product-list li {
    position: relative;
    height: 42.5px;
    padding-left: 28px;
    font-size: 22.5px; font-weight: 700;
    text-transform: uppercase;
    line-height: 34px;
    color: var(--dark);
  }
  .product-list li::before {
    content: ""; position: absolute;
    left: 0; top: 12px;
    width: 13px; height: 13px;
    background: var(--blue);
  }
  .product-list li::after {
    content: ""; position: absolute;
    left: 18px; top: 37px;
    width: 287px; height: 1.5px;
    background: var(--blue);
  }
  .website {
    position: absolute;
    left: 58px; top: 362px;
    font-size: 16.5px; font-weight: 400;
  }
</style>
</head>
<body>

<section class="card card--front">
  <svg class="card__swoosh" viewBox="0 0 733 430" aria-hidden="true">
    <path d="M530,0 C470,60 430,150 460,210 C500,275 630,365 733,428 L733,0 Z" fill="#2a2220"/>
    <path d="M545,0 C512,30 505,90 532,125 C585,190 680,272 733,326 L733,0 Z" fill="#00b2dd"/>
  </svg>
  <div class="brand">Vantrel</div>
  <h1 class="holder-name">Ian Farrow</h1>
  <ul class="contact-list">
    <li>
      <svg class="icon" viewBox="0 0 18 18" aria-hidden="true"><circle cx="9" cy="9" r="9" fill="#00b2dd"/><path d="M5.5 4.5 L7.5 4.3 L8.3 6.8 L7.2 7.7 C7.8 9 8.8 10 10.2 10.7 L11.2 9.7 L13.6 10.5 L13.5 12.5 C9 13 5 9 5.5 4.5 Z" fill="#fff"/></svg>
      China : +86 139 5 270 4418
    </li>
    <li>
      <svg class="icon" viewBox="0 0 18 18" aria-hidden="true"><circle cx="9" cy="9" r="9" fill="#00b2dd"/><path d="M5.5 4.5 L7.5 4.3 L8.3 6.8 L7.2 7.7 C7.8 9 8.8 10 10.2 10.7 L11.2 9.7 L13.6 10.5 L13.5 12.5 C9 13 5 9 5.5 4.5 Z" fill="#fff"/></svg>
      Australia : +61 412 570 883
    </li>
    <li>
      <svg class="icon" viewBox="0 0 18 18" aria-hidden="true"><circle cx="9" cy="9" r="9" fill="#00b2dd"/><rect x="4.5" y="5.8" width="9" height="6.4" fill="none" stroke="#fff" stroke-width="1.2"/><path d="M4.5 5.8 L9 9.5 L13.5 5.8" fill="none" stroke="#fff" stroke-width="1.2"/></svg>
      ifarrow@vantrelfittings.com
    </li>
    <li>
      <svg class="icon" viewBox="0 0 18 18" aria-hidden="true"><circle cx="9" cy="9" r="9" fill="#00b2dd"/><circle cx="9" cy="9" r="5" fill="none" stroke="#fff" stroke-width="1.1"/><ellipse cx="9" cy="9" rx="2.2" ry="5" fill="none" stroke="#fff" stroke-width="1"/><path d="M4 9 H14" stroke="#fff" stroke-width="1"/></svg>
      www.vantrelfittings.com
    </li>
  </ul>
  <div class="address">
    <svg class="icon" viewBox="0 0 18 18" aria-hidden="true"><circle cx="9" cy="9" r="9" fill="#00b2dd"/><path d="M9 14 C6.5 10.8 5.5 9.2 5.5 7.5 A3.5 3.5 0 0 1 12.5 7.5 C12.5 9.2 11.5 10.8 9 14 Z" fill="#fff"/><circle cx="9" cy="7.5" r="1.3" fill="#00b2dd"/></svg>
    <p>1208-3, Lan Qiao Building<br>74 Heping Road, Haishu District<br>Ningbo 315000 China</p>
  </div>
</section>

<section class="card card--back">
  <svg class="card__swoosh" viewBox="0 0 733 430" aria-hidden="true">
    <path d="M530,0 C470,60 430,150 460,210 C500,275 630,365 733,428 L733,0 Z" fill="#2a2220"/>
    <path d="M545,0 C512,30 505,90 532,125 C585,190 680,272 733,326 L733,0 Z" fill="#00b2dd"/>
  </svg>
  <div class="brand">Vantrel</div>
  <ul class="product-list">
    <li>Hydraulic Adapters</li>
    <li>Hose Fittings</li>
    <li>Quick Couplings</li>
  </ul>
  <p class="website">www.vantrelfittings.com</p>
</section>

</body>
</html>
```